Gutschein-Design für Baumhaus-Vermietung
Zielgruppe
Das Leben in einem Baumhaus verspricht Entspannung, Abenteuer, Entdeckungen, Spaß, Spiel und Naturbeobachtungen. Unsere gemütlichen Baumhäuser bieten Ihnen einen naturverbundenen Urlaub mit vielen aufregenden Erlebnissen.
Aufgabenstellung
Das Logo soll unbedingt verwendet werden. Das Format sollte DIN a4 sein, dass wir es über unseren Drucker erstellen können. Als Angaben auf dem Gutschein zur Identifikation wird eine Gutscheinnummer und ein Ausstellungsdatum benötigt. Dazu unsere Adresse und die Kontaktdaten. Es handelt sich um einen Wertgutschein (der dann als Urlaubscheck eingelöst werden kann)

```html
<!DOCTYPE html>
<html lang="de">
<head>
<meta charset="utf-8">
<title>Wertgutschein – Ferienhof & Waldnesthotel Moosau</title>
<link rel="stylesheet" href="https://fonts.googleapis.com/css2?family=Encode+Sans+Semi+Condensed:wght@400;500;700&family=Kaushan+Script&display=swap">
<style>
  :root {
    --paper: #ffffff;
    --brown: #4a3426;
    --green: #2f6b3a;
    --field: #f8f6ee;
    --text: #4a3a30;
    --wood: #b07a45;
    --forest: #3f6b2f;
    --meadow: #7da44a;
  }
  html, body { margin: 0; padding: 0; overflow: hidden; background: var(--paper); }
  .voucher {
    position: relative; width: 849px; height: 1200px; overflow: hidden;
    background: var(--paper);
    font-family: "Encode Sans Semi Condensed", sans-serif; color: var(--text);
  }
  .photo { position: absolute; }
  .photo--kitchen { left: 0; top: 0; width: 393px; height: 231px; background: linear-gradient(160deg, #8a5a32 0%, #e9dccb 45%, #b97a44 100%); }
  .photo--treehouse { left: 406px; top: 0; width: 443px; height: 231px; background: linear-gradient(180deg, #3f6b2f 0%, #6a8a3a 55%, #a46f3e 100%); }
  .photo--meadow { left: 0; top: 242px; width: 444px; height: 231px; background: linear-gradient(180deg, #b9d3e4 0%, #3e6a34 40%, #7aa548 75%, #5c8a35 100%); }
  .photo--bedroom { left: 456px; top: 242px; width: 393px; height: 231px; background: linear-gradient(160deg, #7a4a24 0%, #c9874a 45%, #efe6d8 80%, #b07a45 100%); }
  .slogan { position: absolute; top: 160px; margin: 0; font-family: "Kaushan Script", cursive; color: #fff; font-weight: 400; line-height: 1; }
  .slogan--main { left: 218px; font-size: 68px; }
  .slogan--sub { left: 414px; top: 190px; font-size: 40px; }
  .frame { position: absolute; left: 0; top: 0; pointer-events: none; }
  .title { position: absolute; left: 85px; top: 500px; margin: 0; font-size: 55px; font-weight: 400; color: var(--brown); letter-spacing: 0.5px; line-height: 1; }
  .label { position: absolute; font-size: 13px; color: var(--brown); }
  .field { position: absolute; background: var(--field); border-radius: 8px; }
  .note { position: absolute; left: 561px; top: 843px; margin: 0; font-size: 11.5px; line-height: 16px; color: var(--brown); }
  .brand { position: absolute; left: 40px; top: 1000px; display: flex; align-items: center; gap: 12px; }
  .brand__dot { width: 56px; height: 56px; border-radius: 50%; background: var(--brown); }
  .brand__name { font-size: 26px; font-weight: 700; color: var(--green); line-height: 1.1; }
  .contact { position: absolute; left: 406px; top: 1030px; }
  .contact__name { margin: 0 0 14px; font-size: 17px; font-weight: 700; color: var(--green); }
  .contact__line { margin: 0; font-size: 13.5px; line-height: 18.5px; color: var(--brown); letter-spacing: 0.2px; }
  .social { position: absolute; left: 756px; width: 24px; height: 24px; border-radius: 50%; background: var(--brown); }
</style>
</head>
<body>
<div class="voucher">
  <div class="photo photo--kitchen" role="img" aria-label="Foto: helle Ferienwohnung mit Holzbalken, Küche und Essplatz"></div>
  <div class="photo photo--treehouse" role="img" aria-label="Foto: Baumhaus aus Holz zwischen Bäumen mit Treppe und Terrasse"></div>
  <div class="photo photo--meadow" role="img" aria-label="Foto: zwei Kinder laufen über eine frisch gemähte Wiese am Waldrand"></div>
  <div class="photo photo--bedroom" role="img" aria-label="Foto: gemütliches Schlafzimmer im Baumhaus mit Holzverkleidung und Doppelbett"></div>

  <p class="slogan slogan--main">Natur</p>
  <p class="slogan slogan--sub">erleben</p>

  <svg class="frame" width="849" height="1200" viewBox="0 0 849 1200" aria-hidden="true">
    <polyline points="49,912 49,49 800,49 800,1150 376,1150" fill="none" stroke="#2f6b3a" stroke-width="1.2"/>
  </svg>

  <h1 class="title">WERTGUTSCHEIN</h1>

  <span class="label" style="left:101px; top:603px;">Gutscheinwert in EUR</span>
  <div class="field" style="left:89px; top:622px; width:206px; height:48px;"></div>
  <span class="label" style="left:329px; top:603px;">Gutschein für</span>
  <div class="field" style="left:324px; top:622px; width:419px; height:48px;"></div>

  <span class="label" style="left:101px; top:683px;">Persönliche Widmung</span>
  <div class="field" style="left:89px; top:702px; width:654px; height:94px;"></div>

  <span class="label" style="left:101px; top:805px;">Gutschein-Nr.:</span>
  <div class="field" style="left:89px; top:824px; width:206px; height:48px;"></div>
  <span class="label" style="left:339px; top:805px;">Ausstellungsdatum</span>
  <div class="field" style="left:324px; top:824px; width:209px; height:48px;"></div>

  <p class="note">Der Gutschein ist 3 Jahre gültig und<br>zu allen Saisonzeiten einlösbar.</p>

  <div class="brand">
    <div class="brand__dot"></div>
    <div class="brand__name">Ferienhof &amp;<br>Waldnesthotel Moosau</div>
  </div>

  <div class="contact">
    <p class="contact__name">Ferienhof &amp; Waldnesthotel Moosau</p>
    <p class="contact__line">Familie Lindmayr</p>
    <p class="contact__line">Moosweg 12 | 87400 Tannried</p>
    <p class="contact__line">+49 (0)8300 5550123 | info@waldnesthotel-moosau.de</p>
  </div>

  <div class="social" style="top:1033px;"></div>
  <div class="social" style="top:1068px;"></div>
</div>
</body>
</html>
```